Square graphic for social media post

I want to create a 1080 x 1080px all-black image for the quote below that I can share on social media. I want the emphasis to be primarily on the quote, secondarily on the portrait, and third (smallest) on the logo. I want the background on the portrait to be edited so it's transparent and just shows the face of the person on a black background (no brick wall visible).

Graphic color: black
Text color: white
Content: "What we went through is going to make the greatest generation of hoteliers our industry has ever seen." << biggest text
Dorian Welk << smaller text
President, Marrowgate Hotels << smaller text
[image of person - use whichever version looks better to you]
[Add Lodging Ledger logo - whichever looks better to you]

This image needs to be readable when sized down much smaller (400x400?) so want the text and portrait to take up most of the space.

I'd like the output both as PNG and original file (preferably Canva). Thanks!

Target Market(s)

Hotel managers

Industry/Entity Type

Hospitality

Font styles to use
Sans Serif

Colors

Designer to choose colors to be used in the design.

Requirements
Must have
• Needs to focus on the quote and the person quoted (the portrait)

```html
<!DOCTYPE html>
<html lang="en">
<head>
<meta charset="utf-8">
<title>Dorian Welk Quote – Lodging Ledger</title>
<link rel="stylesheet" href="https://fonts.googleapis.com/css2?family=Roboto+Condensed:wght@700;800&family=Montserrat:wght@300;400&display=swap">
<style>
  :root {
    --bg: #000000;
    --ink: #ffffff;
    --ink-soft: #e9e9e9;
    --suit: #16213f;
    --skin: #8a5f4c;
    --shirt: #d9d4d2;
  }
  * { margin: 0; padding: 0; box-sizing: border-box; }
  html, body {
    width: 1200px;
    height: 1200px;
    overflow: hidden;
    background: var(--bg);
  }
  .post {
    position: relative;
    width: 1200px;
    height: 1200px;
    background: var(--bg);
    color: var(--ink);
    overflow: hidden;
  }
  .portrait {
    position: absolute;
    left: 740px;
    top: 140px;
    width: 460px;
    height: 980px;
    background:
      radial-gradient(ellipse 110px 140px at 230px 175px, var(--skin) 0%, rgba(138,95,76,0.85) 55%, rgba(138,95,76,0) 100%),
      radial-gradient(ellipse 70px 260px at 230px 520px, var(--shirt) 0%, rgba(217,212,210,0.6) 50%, rgba(217,212,210,0) 100%),
      radial-gradient(ellipse 250px 520px at 240px 560px, var(--suit) 0%, rgba(22,33,63,0.7) 55%, rgba(0,0,0,0) 100%);
    -webkit-mask-image: linear-gradient(to bottom, #000 0%, #000 55%, transparent 100%);
            mask-image: linear-gradient(to bottom, #000 0%, #000 55%, transparent 100%);
  }
  .quote {
    position: absolute;
    left: 83px;
    top: 380px;
    width: 1060px;
  }
  .quote__mark {
    display: block;
    width: 106px;
    height: 80px;
    margin-bottom: 50px;
  }
  .quote__text {
    font-family: "Roboto Condensed", "Arial Narrow", sans-serif;
    font-weight: 700;
    font-size: 45px;
    line-height: 57px;
    letter-spacing: 0.5px;
    text-transform: uppercase;
    color: var(--ink);
  }
  .attribution {
    position: absolute;
    left: 83px;
    top: 730px;
    font-family: "Montserrat", "Helvetica Neue", sans-serif;
    color: var(--ink);
  }
  .attribution__name {
    font-weight: 300;
    font-size: 37px;
    letter-spacing: 0.5px;
    text-transform: uppercase;
    line-height: 1;
  }
  .attribution__role {
    margin-top: 22px;
    font-weight: 400;
    font-size: 18px;
    letter-spacing: 0.3px;
    text-transform: uppercase;
    color: var(--ink-soft);
  }
  .brand {
    position: absolute;
    right: 60px;
    bottom: 42px;
    font-family: "Roboto Condensed", "Arial Narrow", sans-serif;
    font-weight: 700;
    font-size: 20px;
    letter-spacing: 1px;
    text-transform: uppercase;
    color: var(--ink);
  }
</style>
</head>
<body>
  <main class="post">
    <div class="portrait" role="img" aria-label="Portrait of Dorian Welk, smiling, in a navy blazer and white open-collar shirt on a black background"></div>

    <blockquote class="quote">
      <svg class="quote__mark" viewBox="0 0 106 80" aria-hidden="true">
        <path fill="#ffffff" d="M4 80 V46 C4 20 16 5 44 0 L47 12 C32 17 26 26 25 38 H46 V80 Z"/>
        <path fill="#ffffff" d="M60 80 V46 C60 20 72 5 100 0 L103 12 C88 17 82 26 81 38 H102 V80 Z"/>
      </svg>
      <p class="quote__text">What we went through is going<br>to make the greatest generation<br>of hoteliers our industry has ever seen.</p>
    </blockquote>

    <div class="attribution">
      <p class="attribution__name">Dorian Welk</p>
      <p class="attribution__role">President, Marrowgate Hotels</p>
    </div>

    <p class="brand">Lodging Ledger</p>
  </main>
</body>
</html>
```